Zarqa Fowl "The Tender Path"

I need a business card design and a logo design for my business. It's a delivery business of halal poultry (chicken). I would the business card to include the following information.
-business name: Zarqa Fowl
-business tag line: "The Tender Path"
Name: Tariq Moussef
Contact number: 07812450937
E-mail: zarqa_fowl@mailbox-example.com
Website: www.zarqafowl-example.com
Also need a business logo also included relating to the business.
I would like it professional yet creative. Something original. I want it to have 2 main colours included.
I want it to have a middle Eastern/ Arabic look if possible.
Thanks :)
Target Market(s)
Butchers
Restaurants
Industry/Entity Type
Business
Contact Information for Business Card
Business name: Zarqa fowl
Business tag line: "The Tender Path"
E-mail: zarqa_fowl@mailbox-example.com
Name: Tariq Moussef

```html
<!DOCTYPE html>
<html lang="en">
<head>
<meta charset="utf-8">
<title>Zarqa Fowl — Business Card</title>
<link rel="stylesheet" href="https://fonts.googleapis.com/css2?family=Source+Sans+3:wght@400;700&display=swap">
<style>
  :root {
    --frame-tan: #c4986b;
    --panel: #f2f2f2;
    --stripe: #e6e7e9;
    --ink-brand: #c0966a;
    --ink-text: #a87c52;
    --watermark: #ece8e1;
  }
  html, body {
    margin: 0;
    padding: 0;
    overflow: hidden;
    background: #ffffff;
  }
  .card {
    position: relative;
    width: 1200px;
    height: 686px;
    background: var(--frame-tan);
    overflow: hidden;
    font-family: "Source Sans 3", "Myriad Pro", Arial, sans-serif;
  }
  .frame-stripe {
    position: absolute;
    width: 23px;
    background: var(--stripe);
  }
  .frame-stripe.top { top: 0; height: 25px; }
  .frame-stripe.bottom { bottom: 0; height: 28px; }
  .panel {
    position: absolute;
    left: 30px;
    top: 25px;
    width: 1140px;
    height: 633px;
    background: var(--panel);
    overflow: hidden;
  }
  .watermark {
    position: absolute;
    left: 0;
    top: 0;
  }
  .brand-mark {
    position: absolute;
    left: 158px;
    top: 50px;
    width: 110px;
    height: 110px;
    border-radius: 50%;
    background: var(--ink-brand);
  }
  .brand-name {
    position: absolute;
    left: 31px;
    top: 160px;
    margin: 0;
    font-weight: 700;
    font-size: 56px;
    line-height: 1;
    color: var(--ink-brand);
    letter-spacing: 0.5px;
  }
  .tagline {
    position: absolute;
    left: 75px;
    top: 236px;
    margin: 0;
    font-weight: 400;
    font-size: 28px;
    letter-spacing: 5px;
    color: var(--ink-text);
  }
  .contact-name {
    position: absolute;
    left: 60px;
    top: 373px;
    margin: 0;
    font-weight: 400;
    font-size: 36px;
    color: var(--ink-text);
  }
  .contact-list {
    position: absolute;
    left: 60px;
    top: 432px;
    margin: 0;
    padding: 0;
    list-style: none;
    font-size: 25px;
    line-height: 35px;
    color: var(--ink-text);
  }
</style>
</head>
<body>
  <div class="card">
    <div class="frame-stripe top" style="left:539px"></div>
    <div class="frame-stripe top" style="left:587px"></div>
    <div class="frame-stripe top" style="left:635px"></div>
    <div class="frame-stripe bottom" style="left:539px"></div>
    <div class="frame-stripe bottom" style="left:587px"></div>
    <div class="frame-stripe bottom" style="left:635px"></div>

    <section class="panel">
      <svg class="watermark" width="1140" height="633" viewBox="0 0 1140 633" aria-hidden="true">
        <circle cx="976" cy="318" r="354" fill="var(--watermark)"/>
      </svg>

      <div class="brand-mark" aria-hidden="true"></div>
      <h1 class="brand-name">Zarqa Fowl</h1>
      <p class="tagline">The Tender Path</p>

      <h2 class="contact-name">Tariq Moussef</h2>
      <ul class="contact-list">
        <li>07812450937</li>
        <li>zarqa_fowl@mailbox-example.com</li>
        <li>www.zarqafowl-example.com</li>
      </ul>
    </section>
  </div>
</body>
</html>
```